Modern Quillby Tree Care Website

I need a website for a full service Tree Care company. The company provides tree pruning, tree removal, tree preservation, emergency services, stump grinding, and emergency tree services.

Target Market(s)

Customers that need tree services

Industry/Entity Type

Landscaping, Tree Services

Coding

Coded - Design and coding required

Number of Pages Required

5+ page

Font styles to use
Sans Serif

Requirements
Must have
• Good clean design that showcases the services the company provides.
Nice to have
• Services page; contact form, blog, home page, about page

```html
<!DOCTYPE html>
<html lang="en">
<head>
<meta charset="utf-8">
<title>Quillby Tree Care</title>
<link rel="stylesheet" href="https://fonts.googleapis.com/css2?family=Noto+Sans:wght@400;600;700&family=Open+Sans:wght@400;600;700&family=Tinos&display=swap">
<style>
:root{
  --green:#8cc63f;
  --navy:#0f1f5c;
  --ink:#222;
  --muted:#8a8f99;
  --pale:#f3f6fb;
  --grey:#efefef;
  --dark:#0d1224;
  --forest:#2f4a1f;
}
*{margin:0;padding:0;box-sizing:border-box}
html,body{width:1200px;height:4298px;overflow:hidden}
body{position:relative;font-family:"Open Sans",sans-serif;color:var(--ink);background:#fff}
.abs{position:absolute}
.head{font-family:"Noto Sans",sans-serif;font-weight:700}
.label{font-size:12px;color:var(--green);font-weight:600;text-transform:uppercase;padding-bottom:4px;border-bottom:2px solid var(--green);display:inline-block}
.photo{position:absolute}
/* header */
.topbar{left:0;top:0;width:1200px;height:145px;background:var(--pale)}
.brand{display:flex;align-items:center;gap:12px;font-family:"Noto Sans",sans-serif;font-weight:700;font-size:28px;color:var(--forest)}
.brand .mark{width:44px;height:44px;background:var(--green)}
.contact-chip{display:flex;gap:14px;align-items:center;font-family:Arial,sans-serif;font-size:13px;color:#555;line-height:20px}
.diamond{width:30px;height:30px;border:1px solid #7fd3c3;transform:rotate(45deg);display:flex;align-items:center;justify-content:center}
.diamond span{width:8px;height:8px;border-radius:50%;background:#2cb58f;transform:rotate(-45deg)}
.nav{left:245px;top:112px;width:878px;height:50px;background:#fff;border-radius:25px;font-family:Arial,sans-serif;font-size:14px;color:#333}
.nav a{position:absolute;top:16px;color:#333;text-decoration:none}
.btn-appt{position:absolute;right:0;top:0;width:156px;height:50px;border-radius:25px;background:var(--green);color:#fff;font-size:14px;display:flex;align-items:center;justify-content:center;box-shadow:0 3px 6px rgba(0,0,0,.15)}
/* hero */
.hero{left:0;top:145px;width:1200px;height:905px;background:linear-gradient(90deg,#050505 0%,#1a1f14 35%,#4d6b2b 60%,#7fa146 80%,#56703a 100%)}
.hero-title{left:92px;top:378px;border-left:5px solid var(--green);padding-left:24px;font-size:37px;line-height:50px;color:#fff}
.hero-text{left:120px;top:490px;width:500px;font-size:15px;line-height:29px;color:#fff}
.btn-green{background:var(--green);color:#fff;font-weight:700;display:flex;align-items:center;justify-content:center}
/* about */
.about-title{left:604px;top:1025px;font-size:37px;line-height:47px;color:var(--navy)}
.about-sub{left:604px;top:1142px;font-size:20px;color:var(--navy);font-family:"Noto Sans",sans-serif;font-weight:600}
.about-p{left:604px;width:455px;font-size:12px;line-height:19px;color:var(--muted)}
/* services */
.services{left:0;top:1432px;width:1200px;height:663px;background:var(--grey)}
.section-title{width:1200px;left:0;text-align:center;font-size:42px;color:var(--navy)}
.svc-img{height:280px;width:304px;top:1654px}
.svc-card{top:1881px;width:237px;height:140px;background:#fff;box-shadow:0 4px 12px rgba(0,0,0,.08)}
.svc-card h3{font-family:"Noto Sans",sans-serif;font-size:17px;color:var(--navy);margin:34px 0 0 22px;font-weight:700}
.svc-card p{font-size:12.5px;line-height:21px;color:var(--muted);margin:8px 0 0 22px;width:195px}
.icon-dot{width:60px;height:60px;border-radius:50%;background:var(--green);display:flex;align-items:center;justify-content:center}
/* why */
.why{left:0;top:2095px;width:1200px;height:575px;background:linear-gradient(90deg,#2f4d1c 0%,#4f7a2b 35%,#6b8f3d 50%,#1a1f16 70%,#000 100%)}
.why-title{left:621px;top:2172px;font-size:37px;line-height:47px;color:#fff}
.why-item{left:626px;width:442px;height:104px;background:#1b1b1b;border-left:4px solid var(--green)}
.why-item h4{position:absolute;left:95px;top:23px;font-family:"Noto Sans",sans-serif;font-size:14px;color:#fff;font-weight:700}
.why-item p{position:absolute;left:95px;top:45px;width:320px;font-size:12px;line-height:20px;color:#ddd}
.why-item svg{position:absolute;left:32px;top:32px}
/* testimonials */
.testi{left:0;top:2670px;width:1200px;height:610px;background:var(--pale)}
.quote{top:2897px;width:305px;height:174px;background:#fff;padding:28px 22px;font-size:15px;line-height:23px;color:#444}
.quote.active{background:var(--green);color:#fff}
.quote::after{content:"";position:absolute;left:0;bottom:-18px;border-left:18px solid var(--green);border-bottom:18px solid transparent}
.avatar{top:3097px;width:54px;height:54px;border-radius:50%;background:#c9cdd3;border:3px solid #fff;box-shadow:0 2px 6px rgba(0,0,0,.15)}
.person{top:3100px;font-size:14px;font-family:"Noto Sans",sans-serif;font-weight:700;color:var(--navy);line-height:22px}
.person span{display:block;font-weight:400;font-size:12px;color:var(--muted);font-family:"Open Sans",sans-serif}
/* contact */
.serif{font-family:"Tinos",serif}
.contact-box{left:147px;top:3430px;width:908px;height:292px;background:#fff;box-shadow:0 2px 12px rgba(0,0,0,.08)}
.addr-panel{left:147px;top:3430px;width:304px;height:292px;background:#ececec}
.addr-row{left:178px;display:flex;gap:10px;font-size:14px;line-height:19px;color:#222}
.field{height:1px;background:#888}
.flabel{font-family:Arial,sans-serif;font-size:13px;color:#333}
/* footer */
.footer{left:0;top:3755px;width:1200px;height:543px;background:var(--dark)}
.foot-box{top:4060px;width:271px;height:57px;border-top:6px solid #1f2540;border-bottom:6px solid #1f2540;display:flex;align-items:center;justify-content:center;gap:10px;color:#fff}
.foot-nav{left:0;top:4213px;width:1200px;display:flex;justify-content:center;gap:44px;font-size:13px;color:#fff;font-weight:600}
.social{top:4161px;left:538px;display:flex;gap:8px}
.social span{width:19px;height:19px;border-radius:50%;background:#fff}
</style>
</head>
<body>

<!-- header -->
<div class="abs topbar"></div>
<div class="abs brand" style="left:100px;top:42px"><span class="mark"></span>Quillby Tree Care</div>
<div class="abs contact-chip" style="left:417px;top:34px"><div class="diamond"><span></span></div><div>Email Address<br>office@quillbytree.test</div></div>
<div class="abs contact-chip" style="left:664px;top:34px"><div class="diamond"><span></span></div><div>Email Address<br>office@quillbytree.test</div></div>
<div class="abs contact-chip" style="left:910px;top:34px"><div class="diamond"><span></span></div><div>Email Address<br>office@quillbytree.test</div></div>

<!-- hero -->
<div class="abs hero" role="img" aria-label="Arborist in safety gear roped into a tall tree cutting a trunk"></div>
<svg class="abs" style="left:0;top:790px" width="1200" height="260" viewBox="0 0 1200 260">
  <path d="M0 40 Q520 -40 1200 250 L1200 260 L0 260 Z" fill="#fff"/>
  <path d="M400 30 Q900 10 1200 175 L1200 255 Q950 60 400 30 Z" fill="#8cc63f"/>
</svg>
<nav class="abs nav">
  <a style="left:66px">Home</a><a style="left:156px">About Us</a><a style="left:243px">Services</a><a style="left:325px">Our Team</a><a style="left:426px">Projects</a>
  <div class="btn-appt">Appointment</div>
</nav>
<h1 class="abs head hero-title">We Offer Sustainable<br>Tree Solutions</h1>
<p class="abs hero-text">It is a long and established fact that a reader will be distracted by the readable content of a page when looking.</p>
<div class="abs btn-green" style="left:118px;top:567px;width:197px;height:45px;font-size:14px">REQUEST A DEMO</div>

<!-- about -->
<svg class="abs" style="left:0;top:1010px" width="490" height="422" viewBox="0 0 490 422">
  <defs><clipPath id="aboutClip"><circle cx="210" cy="270" r="240"/></clipPath>
  <linearGradient id="aboutGrad" x1="0" y1="0" x2="1" y2="1"><stop offset="0" stop-color="#9fb0a4"/><stop offset=".5" stop-color="#6d7f5e"/><stop offset="1" stop-color="#3b4a6f"/></linearGradient></defs>
  <rect x="0" y="0" width="445" height="422" fill="url(#aboutGrad)" clip-path="url(#aboutClip)" role="img" aria-label="Climber in blue work gear and yellow helmet working among bare tree branches"/>
  <path d="M250 32 A240 240 0 0 1 400 422" fill="none" stroke="#8cc63f" stroke-width="8"/>
  <circle cx="422" cy="102" r="58" fill="#e9eef3"/>
  <rect x="404" y="84" width="36" height="36" fill="#8cc63f"/>
</svg>
<div class="abs label" style="left:604px;top:993px">Who we are</div>
<h2 class="abs head about-title">Your Partner in Tree<br>Presevation</h2>
<div class="abs about-sub">Enhancing Landscapes, One Tree at a Time</div>
<p class="abs about-p" style="top:1184px">Lorem ipsum dolor sit amet, consectetur adipiscing elit, sed do eiusmod temp or incididunt ut labore et dolore magna aliqua. Ut enim ad minim veniam, quis laboris nisi ut aliquip ex ea commodo consequat.</p>
<p class="abs about-p" style="top:1252px">Lorem ipsum dolor sit amet, consectetur adipiscing elit, sed do eiusmod temp or incididunt ut labore et dolore magna aliqua.</p>
<div class="abs btn-green" style="left:604px;top:1315px;width:136px;height:39px;font-size:14px;gap:14px">Contact us
  <svg width="16" height="12" viewBox="0 0 16 12"><path d="M1 6h13M9 1l5 5-5 5" stroke="#fff" stroke-width="1.6" fill="none"/></svg></div>

<!-- services -->
<div class="abs services"></div>
<div class="abs" style="left:0;width:1200px;top:1522px;text-align:center"><span class="label">Our services</span></div>
<h2 class="abs head section-title" style="top:1555px">Services We Provide</h2>

<div class="photo svc-img" style="left:118px;background:linear-gradient(135deg,#3f6a26,#9bb36a 60,#d9d2c2)" role="img" aria-label="Gardener cutting a branch with red pruning shears"></div>
<div class="photo svc-img" style="left:447px;background:linear-gradient(135deg,#6f8a3c,#8a6a3e 55%,#c9b79a)" role="img" aria-label="Hand touching a freshly cut log in the grass"></div>
<div class="photo svc-img" style="left:774px;background:linear-gradient(135deg,#2d4a22,#5f8d3c 55%,#a8c98a)" role="img" aria-label="Two people inspecting a row of tall hedges"></div>

<div class="abs svc-card" style="left:185px"><h3>Tree Pruning</h3><p>Lorem ipsum dolor sit amet, co nsectetur adipiscing elit, s</p></div>
<div class="abs svc-card" style="left:514px"><h3>Tree Removal</h3><p>Lorem ipsum dolor sit amet, co nsectetur adipiscing elit, s</p></div>
<div class="abs svc-card" style="left:841px"><h3>Stump Grinding</h3><p>Lorem ipsum dolor sit amet, co nsectetur adipiscing elit, s</p></div>
<div class="abs icon-dot" style="left:155px;top:1851px"><svg width="26" height="26" viewBox="0 0 26 26" fill="none" stroke="#fff" stroke-width="1.6"><circle cx="13" cy="8" r="4"/><path d="M4 23c2-6 5-9 9-9s7 3 9 9M10 18l6 5"/></svg></div>
<div class="abs icon-dot" style="left:484px;top:1851px"><svg width="26" height="26" viewBox="0 0 26 26" fill="none" stroke="#fff" stroke-width="1.6"><circle cx="13" cy="8" r="4"/><path d="M4 23c2-6 5-9 9-9s7 3 9 9M10 18l6 5"/></svg></div>
<div class="abs icon-dot" style="left:811px;top:1851px"><svg width="26" height="26" viewBox="0 0 26 26" fill="none" stroke="#fff" stroke-width="1.6"><circle cx="13" cy="8" r="4"/><path d="M4 23c2-6 5-9 9-9s7 3 9 9M10 18l6 5"/></svg></div>

<!-- why choose us -->
<div class="abs why" role="img" aria-label="Sunny lawn with large trees and a house in the background"></div>
<div class="abs label" style="left:621px;top:2143px;font-size:11px">Why choose us</div>
<h2 class="abs head why-title">Your Tree Care<br>Professionals</h2>
<div class="abs why-item" style="top:2287px">
  <svg width="38" height="38" viewBox="0 0 38 38" fill="none" stroke="#fff" stroke-width="1.6"><circle cx="19" cy="11" r="6"/><path d="M5 34c3-9 8-13 14-13s11 4 14 13M15 27l8 7"/></svg>
  <h4>CLIENT-CENTRIC</h4><p>Lorem ipsum dolor sit amet, consectetur adipiscing elit, sed do eiusmod tempor incidid</p></div>
<div class="abs why-item" style="top:2398px">
  <svg width="38" height="38" viewBox="0 0 38 38" fill="none" stroke="#fff" stroke-width="1.6"><path d="M19 4l12 8-3 16H10L7 12z"/><circle cx="19" cy="18" r="5"/></svg>
  <h4>PROFESSIONALISM</h4><p>Lorem ipsum dolor sit amet, consectetur adipiscing elit, sed do eiusmod tempor incidid</p></div>
<div class="abs why-item" style="top:2510px">
  <svg width="38" height="38" viewBox="0 0 38 38" fill="none" stroke="#fff" stroke-width="1.6"><path d="M8 32a15 15 0 1 1 22 0"/><path d="M19 19l6-7"/><circle cx="19" cy="19" r="2"/></svg>
  <h4>EXPERIENCED EXPERTS</h4><p>Lorem ipsum dolor sit amet, consectetur adipiscing elit, sed do eiusmod tempor incidid</p></div>

<!-- testimonials -->
<div class="abs testi"></div>
<div class="abs" style="left:0;width:1200px;top:2764px;text-align:center"><span class="label">Testimonials</span></div>
<h2 class="abs head section-title" style="top:2797px">What Clients are Saying</h2>
<div class="abs quote" style="left:118px">Lorem ipsum dolor sit amet, consectetur adipiscing elit, sed d o eiusmod tempor incididunt ut lab ore et dolore magna aliqua. Ut enim ad min</div>
<div class="abs quote active" style="left:447px">Lorem ipsum dolor sit amet, consectetur adipiscing elit, sed d o eiusmod tempor incididunt ut lab ore et dolore magna aliqua. Ut enim ad min</div>
<div class="abs quote" style="left:776px">Lorem ipsum dolor sit amet, consectetur adipiscing elit, sed d o eiusmod tempor incididunt ut lab ore et dolore magna aliqua. Ut enim ad min</div>
<div class="abs avatar" style="left:137px" role="img" aria-label="Client portrait"></div>
<div class="abs avatar" style="left:465px" role="img" aria-label="Client portrait"></div>
<div class="abs avatar" style="left:795px" role="img" aria-label="Client portrait"></div>
<div class="abs person" style="left:210px">Rowan Hale<span>Engineer</span></div>
<div class="abs person" style="left:538px">Rowan Hale<span>Engineer</span></div>
<div class="abs person" style="left:869px">Rowan Hale<span>Engineer</span></div>
<svg class="abs" style="left:568px;top:3197px" width="64" height="12" viewBox="0 0 64 12"><rect x="0" y="2" width="22" height="8" rx="4" fill="#8cc63f"/><circle cx="32" cy="6" r="4" fill="#8cc63f"/><circle cx="45" cy="6" r="4" fill="#8cc63f"/><circle cx="58" cy="6" r="4" fill="#8cc63f"/></svg>

<!-- contact -->
<h2 class="abs serif" style="left:0;width:1200px;top:3325px;text-align:center;font-size:44px;font-weight:400;color:#333">Get In <span style="color:#2a7fd4">Touch</span></h2>
<div class="abs contact-box"></div>
<div class="abs addr-panel"></div>
<div class="abs serif" style="left:180px;top:3450px;font-size:34px;color:#333">Address</div>
<div class="abs addr-row" style="top:3530px"><svg width="20" height="20" viewBox="0 0 20 20" fill="none" stroke="#8cc63f" stroke-width="1.4"><circle cx="10" cy="6" r="3"/><path d="M3 18c1-5 4-7 7-7s6 2 7 7"/></svg><div>Company Name<br>Place 2134 Ave<br>City, Country</div></div>
<div class="abs addr-row" style="top:3600px;font-weight:700;font-size:13px"><svg width="20" height="20" viewBox="0 0 20 20" fill="none" stroke="#8cc63f" stroke-width="1.4"><path d="M4 2l4 1 1 4-2 1a10 10 0 0 0 5 5l1-2 4 1 1 4c-8 1-15-6-14-14z"/></svg><div>555-014-2290 Or 555-014-7731</div></div>
<div class="abs addr-row" style="top:3640px;font-size:13px"><svg width="20" height="20" viewBox="0 0 20 20" fill="none" stroke="#8cc63f" stroke-width="1.4"><rect x="3" y="2" width="14" height="16"/><circle cx="10" cy="8" r="2.5"/><path d="M6 15c1-3 7-3 8 0"/></svg><div>hello@quillbytree.test</div></div>
<div class="abs flabel" style="left:471px;top:3480px">Name:</div>
<div class="abs field" style="left:471px;top:3497px;width:267px"></div>
<div class="abs field" style="left:771px;top:3497px;width:267px"></div>
<div class="abs flabel" style="left:471px;top:3526px">Phone:</div>
<div class="abs field" style="left:471px;top:3543px;width:267px"></div>
<div class="abs field" style="left:771px;top:3543px;width:267px"></div>
<div class="abs flabel" style="left:471px;top:3569px">Details:</div>
<div class="abs field" style="left:471px;top:3610px;width:565px"></div>
<div class="abs serif" style="left:472px;top:3643px;width:187px;height:37px;border-radius:19px;background:var(--green);color:#fff;font-size:14px;display:flex;align-items:center;justify-content:center;gap:10px">QUICK ENQUIRY
  <svg width="14" height="12" viewBox="0 0 14 12"><path d="M1 6h11M7 1l5 5-5 5" stroke="#fff" stroke-width="1.5" fill="none"/></svg></div>

<!-- footer -->
<div class="abs footer"></div>
<svg class="abs" style="left:0;top:3660px" width="1200" height="300" viewBox="0 0 1200 300">
  <path d="M0 0 Q120 180 740 260 L1200 250 L1200 95 L0 95 Z" fill="#0d1224" opacity="0"/>
  <path d="M0 140 Q300 270 1200 250 L1200 300 L0 300 Z" fill="#0d1224"/>
  <path d="M0 0 Q100 180 740 262 Q250 250 0 80 Z" fill="#8cc63f"/>
  <path d="M0 95 Q200 240 740 262 Q950 270 1200 250 L1200 300 L0 300 Z" fill="#0d1224"/>
</svg>
<div class="abs brand" style="left:0;width:1200px;top:4030px;justify-content:center;color:#fff;font-size:32px"><span class="mark" style="background:#fff;width:48px;height:48px"></span>Quillby Tree Care</div>
<div class="abs foot-box" style="left:175px;font-size:12px;line-height:16px"><svg width="14" height="20" viewBox="0 0 14 20"><path d="M7 0a7 7 0 0 1 7 7c0 5-7 13-7 13S0 12 0 7a7 7 0 0 1 7-7z" fill="#8cc63f"/><circle cx="7" cy="7" r="2.5" fill="#0d1224"/></svg><div>48 BIRCHWOOD LANE<br>COUNTRY</div></div>
<div class="abs foot-box" style="left:761px;font-size:21px"><svg width="14" height="20" viewBox="0 0 14 20"><path d="M7 0a7 7 0 0 1 7 7c0 5-7 13-7 13S0 12 0 7a7 7 0 0 1 7-7z" fill="#8cc63f"/><circle cx="7" cy="7" r="2.5" fill="#0d1224"/></svg>555 014 2290</div>
<div class="abs" style="left:0;width:1200px;top:4128px;text-align:center;font-size:12px;color:var(--green)">hello@quillbytree.test</div>
<div class="abs social"><span></span><span></span><span></span><span></span><span></span></div>
<div class="abs foot-nav"><span>HOME</span><span>SERVICES</span><span>ABOUT US</span><span>PROJECTS</span><span>TESTIMONIALS</span><span>FAQ</span><span>CONTACT US</span></div>

</body>
</html>
```